Revamping and duplicating of existing business card

We are a painting and decorating business based in London and need a couple of business cards made up for the following people.

1. Maribel Osgood
2. Tobias Penrick

Measurements - 85 X 55 mm
Font: Blue highway
Colour: No idea! Would be great to have a pantone for the pink if possible?

I’ve attached all the logos and old artwork etc.
Here are the amendments I would definitely like...

1. Maribel

format mobile number correctly: 07512 368 904

Add title: Decorator
Use: Osgood Decorating Logo
Add twitter logo & @osgooddecor
Add tradevouch logo
Add HFG Logo
Make it all look beautiful/revamp/tweak - whatever you think…

2. Tobias

Decorator

07643 295 581
tobias@osgooddecorating.co.uk
Updates

Hello! Thanks so much for all your designs. This is such a great way to get these things done... Just to clarify, Please do not alter our logo at all. The 'splat' appears on our van, tshirts, quotes etc and is very much part of our branding. Colour scheme: Pink, black and white. Thanks Maribel

Project Deadline Extended
Reason: Not 100% sold on any of the designs so far but very grateful for all the submissions. Keep it simple and quirky please. Thanks Maribel

Industry/Entity Type

Painting

Requirements
Must have
• Pink & Black Colour scheme
Osgood Decorating Logo
Blue Highway font

```html
<!DOCTYPE html>
<html lang="en">
<head>
<meta charset="utf-8">
<title>Osgood Decorating – Maribel – Business Card</title>
<link rel="stylesheet" href="https://fonts.googleapis.com/css2?family=Catamaran:wght@800&family=Questrial&display=swap">
<style>
  :root {
    --brand-pink: #d81b68;
    --soft-pink: #f3c4d6;
    --ink: #111111;
    --paper: #ffffff;
    --listing-red: #e0262b;
    --badge-navy: #2b3a8c;
    --social-blue: #4fc3ec;
  }
  html, body {
    margin: 0;
    padding: 0;
    overflow: hidden;
    background: var(--paper);
  }
  .card {
    position: relative;
    width: 1200px;
    height: 777px;
    overflow: hidden;
    background: var(--paper);
    font-family: "Questrial", sans-serif;
    color: var(--ink);
  }
  .card__art {
    position: absolute;
    inset: 0;
  }
  .brand {
    position: absolute;
    left: 22px;
    top: 6px;
    margin: 0;
    font-family: "Catamaran", sans-serif;
    font-weight: 800;
    color: var(--ink);
    line-height: 0.95;
  }
  .brand__first { display: block; font-size: 118px; letter-spacing: 1px; }
  .brand__second { display: block; font-size: 88px; letter-spacing: 1px; }
  .person {
    position: absolute;
    right: 8px;
    top: 180px;
    text-align: right;
  }
  .person__name {
    margin: 0;
    font-family: "Catamaran", sans-serif;
    font-weight: 800;
    font-size: 88px;
    line-height: 1;
  }
  .person__role {
    margin: 0;
    font-family: "Catamaran", sans-serif;
    font-weight: 800;
    font-size: 42px;
    line-height: 1.1;
  }
  .contact {
    position: absolute;
    right: 12px;
    top: 428px;
    text-align: right;
    font-style: normal;
    font-size: 52px;
    line-height: 1.22;
  }
  .contact a { color: inherit; text-decoration: none; display: block; }
  .membership {
    position: absolute;
    left: 160px;
    top: 640px;
    width: 500px;
  }
  .membership__lead {
    display: block;
    margin-left: 146px;
    font-size: 24px;
  }
  .membership__name {
    display: block;
    font-size: 66px;
    line-height: 1;
    color: var(--listing-red);
  }
  .social {
    position: absolute;
    left: 696px;
    top: 648px;
    display: flex;
    align-items: center;
    gap: 14px;
  }
  .social__mark {
    width: 108px;
    height: 108px;
    border-radius: 10px;
    background: var(--social-blue);
  }
  .social__handle { font-size: 48px; white-space: nowrap; }
</style>
</head>
<body>
<main class="card">
  <svg class="card__art" width="1200" height="777" viewBox="0 0 1200 777">
    <defs>
      <radialGradient id="splash-main" cx="0.5" cy="0.5" r="0.5">
        <stop offset="0.72" stop-color="#d81b68"/>
        <stop offset="1" stop-color="#d81b68" stop-opacity="0"/>
      </radialGradient>
      <radialGradient id="splash-soft" cx="0.5" cy="0.5" r="0.5">
        <stop offset="0.6" stop-color="#f3c4d6"/>
        <stop offset="1" stop-color="#f3c4d6" stop-opacity="0"/>
      </radialGradient>
      <radialGradient id="splash-small" cx="0.5" cy="0.5" r="0.5">
        <stop offset="0.75" stop-color="#d81b68"/>
        <stop offset="1" stop-color="#d81b68" stop-opacity="0"/>
      </radialGradient>
    </defs>
    <ellipse cx="660" cy="420" rx="250" ry="250" fill="url(#splash-soft)" role="img" aria-label="Soft pink paint splash decoration"/>
    <ellipse cx="280" cy="220" rx="420" ry="360" fill="url(#splash-main)" role="img" aria-label="Pink paint splash decoration"/>
    <ellipse cx="960" cy="260" rx="110" ry="130" fill="url(#splash-small)" role="img" aria-label="Small pink paint splash decoration"/>
    <circle cx="82" cy="696" r="60" fill="var(--badge-navy)" role="img" aria-label="HFG membership badge"/>
  </svg>

  <h1 class="brand">
    <span class="brand__first">Osgood</span>
    <span class="brand__second">Decorating</span>
  </h1>

  <section class="person">
    <p class="person__name">Maribel</p>
    <p class="person__role">Decorator</p>
  </section>

  <address class="contact">
    <a href="tel:07512368904">07512 368 904</a>
    <a href="mailto:Maribel@osgooddecorating.co.uk">Maribel@osgooddecorating.co.uk</a>
  </address>

  <div class="membership">
    <span class="membership__lead">Proud members of</span>
    <span class="membership__name">tradevouch</span>
  </div>

  <div class="social">
    <span class="social__mark" aria-hidden="true"></span>
    <span class="social__handle">@osgooddecor</span>
  </div>
</main>
</body>
</html>
```